Flyer for Compassion training days

I need a A5-size, single-sided flyer design for my training days. They are weekends in a blend of Compassionate Communication and Buddhist teachings called Palomere Communication. The logo for Palomere that should be included.
The flyer needs room for 1) course title, 2) course dates, location & price, 3) course description, 4) booking info, 5) my picture & short bio, and 6) the palomere.co website (yes, it is 'co' and not 'com).
Updates

Target Market(s)

Women 35-65 years, well-educated, spiritually minded. May have interests like yoga and meditation.

Industry/Entity Type

Health And Wellness

Font styles to use
Sans Serif
Other font styles liked:
• Blue Plaque, Josefina are both great

Colors
fbf289
fdf9cf
cfeae6
33b8a4

Requirements
Must have
• The Palomere logo; my picture.
• Elegance. Calm and expansive feel.
• The poster provided in the project files shows you the kind of information I need to include.
• Colours -- greens and yellows, but the options on pixel harbor are not quite the right shades.
• The logo colour can be changed.
Nice to have
• Classy (but not cliche) image associated with Buddhism; gentle curves similar to those on the business card (see project files).
Should not have
• Dark background. Busy, loud design. Overly 'swirly' design. Images that I have to buy separately.

```html
<!DOCTYPE html>
<html lang="en">
<head>
<meta charset="utf-8">
<title>Palomere Communication – Core Course Flyer</title>
<link rel="stylesheet" href="https://fonts.googleapis.com/css2?family=Josefin+Sans:wght@400;600;700&display=swap">
<style>
  :root{
    --page:#e9ebe8;
    --paper:#ffffff;
    --paper-mist:#eeeeec;
    --teal:#33b8a4;
    --teal-deep:#2aa493;
    --ink:#2c2b2a;
    --ink-soft:#3b3a38;
    --brown:#2f2522;
    --gold:#d69a2c;
    --gold-light:#f3cf6a;
    --strip:#dcdcdb;
  }
  *{box-sizing:border-box;margin:0;padding:0}
  html,body{width:1200px;height:1199px;overflow:hidden;background:var(--page)}
  body{font-family:"Josefin Sans",sans-serif;color:var(--ink)}
  .flyer{
    position:absolute;left:216px;top:45px;width:768px;height:1090px;
    background:radial-gradient(ellipse at 60% 55%,#f7f7f6 0%,var(--paper-mist) 70%,#e4e4e2 100%);
    overflow:hidden;box-shadow:0 6px 24px rgba(0,0,0,.18);
  }
  .hero{position:absolute;left:0;top:0;width:768px;height:240px}
  .statue{
    position:absolute;left:545px;top:108px;width:170px;height:192px;
    border-radius:48% 48% 40% 40%;
    background:radial-gradient(ellipse at 50% 40%,var(--gold-light) 0%,var(--gold) 55%,#a8701c 100%);
  }
  .equation{position:absolute;left:65px;top:242px;width:440px;font-size:27px;line-height:33px;text-align:center;color:var(--ink)}
  .equation .accent{color:var(--teal)}
  .title{position:absolute;left:64px;top:312px;width:690px;font-size:55px;font-weight:400;white-space:nowrap;letter-spacing:-.5px;line-height:64px}
  .tag{
    position:absolute;background:var(--teal);color:#fff;
    border-radius:14px 0 14px 0;
  }
  .tag-course{left:45px;top:390px;width:192px;height:51px;font-size:29px;line-height:56px;text-align:center}
  .brand-mark{position:absolute;left:55px;top:515px;width:180px;display:flex;align-items:center;gap:10px;font-size:30px;font-weight:600;color:var(--teal)}
  .brand-mark .dot{width:22px;height:22px;border-radius:50%;background:var(--teal);flex:none}
  .event-info{position:absolute;left:67px;top:643px;font-weight:600;color:var(--ink-soft)}
  .event-info p{font-size:21px;line-height:27px}
  .event-info .event-date{font-size:30px;line-height:36px;font-weight:700;margin-bottom:2px}
  .event-info .event-price{font-size:24px;margin-top:4px}
  .event-web{position:absolute;left:54px;top:774px;font-size:23px;font-weight:600;color:var(--ink-soft)}
  .body{position:absolute;left:260px;width:460px;color:var(--ink-soft)}
  .intro{top:390px;font-size:19px;line-height:26px}
  .explore-head{top:535px;font-size:23px}
  .checklist{top:575px;list-style:none;font-size:17px;line-height:22px;font-weight:600}
  .checklist li{position:relative;padding-left:27px;margin-bottom:6px}
  .checklist svg{position:absolute;left:0;top:3px}
  .audience{top:719px;font-size:17.5px;line-height:24px}
  .tag-booking{left:259px;top:849px;width:108px;height:30px;font-size:21px;line-height:33px;text-align:center;border-radius:10px 0 10px 0}
  .booking-text{position:absolute;left:387px;top:852px;font-size:19px;line-height:24px;font-weight:600}
  .booking-text a{color:var(--teal-deep);text-decoration:none}
  .portrait{
    position:absolute;left:36px;top:828px;width:184px;height:184px;border-radius:50%;
    border:3px solid var(--brown);
    background:radial-gradient(circle at 50% 40%,#b9a899 0%,#7d6a5b 60%,#4a3b32 100%);
  }
  .facilitator-bar{position:absolute;left:195px;top:901px;width:172px;height:28px;background:var(--brown);color:#fff;font-size:20px;line-height:31px;text-align:right;padding-right:12px}
  .bio{position:absolute;left:276px;top:910px;width:450px;font-size:17.5px;line-height:24px;color:var(--ink-soft)}
  .bio .lead{text-indent:104px}
  .bio .coaching{font-weight:600;margin-top:5px;white-space:nowrap}
  .foot-strip{position:absolute;left:0;bottom:0;width:768px;height:26px;background:var(--strip)}
</style>
</head>
<body>
<main class="flyer">
  <svg class="hero" viewBox="0 0 768 240" width="768" height="240">
    <defs>
      <linearGradient id="templeTone" x1="0" y1="0" x2="1" y2="0">
        <stop offset="0" stop-color="#6e3d24"/>
        <stop offset=".45" stop-color="#c9812b"/>
        <stop offset="1" stop-color="#e9a45b"/>
      </linearGradient>
    </defs>
    <path role="img" aria-label="Photograph of a row of golden Buddha statues in a temple" fill="url(#templeTone)"
      d="M0 0H768V178C640 178 540 200 420 205C260 210 120 160 0 140Z"/>
    <path fill="var(--teal)" d="M0 140C120 160 260 210 420 205C540 200 640 178 768 178V198C640 196 540 214 420 220C260 226 110 188 0 168Z"/>
    <path fill="#f4f4f2" d="M0 168C110 188 260 226 420 220C540 214 640 196 768 198V240H0Z"/>
  </svg>
  <div class="statue" role="img" aria-label="Photograph of a seated golden Buddha statue"></div>

  <p class="equation">Mindfulness + <span class="accent">Kindness +</span><br>Compassionate Communication =</p>
  <h1 class="title">Palomere Communication</h1>

  <div class="tag tag-course">Core Course</div>
  <div class="brand-mark"><span class="dot"></span>Palomere</div>

  <div class="event-info">
    <p class="event-date">11-12 Dec</p>
    <p>Hawthorn Centre,</p>
    <p>Edinburgh</p>
    <p class="event-price">£125/100</p>
  </div>
  <p class="event-web">www.palomere.co</p>

  <p class="body intro">Palomere Communication can help you increase awareness &amp; compassion in everyday speech (with yourself &amp; others), better understand your own patterns, and build resilience to challenging situations. Choose from:</p>
  <p class="body explore-head">In this 2-day Core Course, we’ll explore:</p>
  <ul class="body checklist">
    <li><svg width="16" height="14" viewBox="0 0 16 14"><path d="M1 7l5 5L15 1" fill="none" stroke="#33b8a4" stroke-width="2"/></svg>Compassionate Communication;</li>
    <li><svg width="16" height="14" viewBox="0 0 16 14"><path d="M1 7l5 5L15 1" fill="none" stroke="#33b8a4" stroke-width="2"/></svg>Buddhist teachings on Right Speech, loving-kindness, Right Effort, and more;</li>
    <li><svg width="16" height="14" viewBox="0 0 16 14"><path d="M1 7l5 5L15 1" fill="none" stroke="#33b8a4" stroke-width="2"/></svg>mindfulness practices;</li>
    <li><svg width="16" height="14" viewBox="0 0 16 14"><path d="M1 7l5 5L15 1" fill="none" stroke="#33b8a4" stroke-width="2"/></svg>choices available to us in our everyday speech.</li>
  </ul>
  <p class="body audience">This workshop will be of interest if you’d like to improve personal and/or professional relationships.&nbsp; Open to all, best suited to those with at least 1 year’s experience with Mindfulness,&nbsp; Buddhism, or Compassionate Communication / NVC.</p>

  <div class="tag tag-booking">booking</div>
  <p class="booking-text">Book online at Ticketnest or<br>write <a href="mailto:marisol@palomere.co">marisol@palomere.co</a></p>

  <div class="portrait" role="img" aria-label="Portrait photograph of the course facilitator"></div>
  <div class="facilitator-bar">facilitator</div>
  <div class="bio">
    <p class="lead">Marisol Fenwick is an experienced group facilitator, having worked with a range of organisations and presented at a number of festivals &amp; conferences.</p>
    <p class="coaching">Marisol offers coaching in Palomere Communication.</p>
  </div>

  <div class="foot-strip"></div>
</main>
</body>
</html>
```